Modern corporate energy/fuel business need business card design

Business card required for company founder. Korvan Fuel Partners is a Australian based modern energy/fuel provider. We offer specialised solutions to businesses using fossil fuels through renewable energy solutions.

I would like one side with specific information (name, address etc)

The other side to be bold, professional company name & logo. Striking.

Target Market(s)

B2B. Transport, mining, councils, environmentalist,

Industry/Entity Type

Petroleum

Contact Information for Business Card

Name; Peter Morrow
Position; Director
Email; pmorrow@korvanse.com.au
Address; PO Box 347, Larkvale, QLD, 4812
Website; www.korvanse.com.au

Colors

Designer to choose colors to be used in the design.

Requirements
Must have
• Clean, easy to read, professional & strong theme
Should not have
• too many colours, busy layout,

```html
<!DOCTYPE html>
<html lang="en">
<head>
<meta charset="utf-8">
<title>Korvan Fuel Partners – Business Card</title>
<link rel="stylesheet" href="https://fonts.googleapis.com/css2?family=Open+Sans:wght@400;600&display=swap">
<style>
  :root {
    --backdrop: #bcdcba;
    --card-white: #ffffff;
    --brand-orange: #f07a2c;
    --brand-orange-light: #f9b98a;
    --brand-navy: #1f4f78;
    --text-grey: #5a5f66;
    --rule-grey: #9aa0a6;
  }
  * { box-sizing: border-box; margin: 0; padding: 0; }
  html, body {
    width: 1200px; height: 1200px; overflow: hidden;
    background: var(--backdrop);
    font-family: "Open Sans", Arial, sans-serif;
  }
  .sheet {
    width: 1200px; height: 1200px;
    display: flex; flex-direction: column; align-items: center; justify-content: center;
    gap: 60px;
  }
  .card {
    width: 840px; height: 480px; position: relative; overflow: hidden;
    box-shadow: 0 10px 28px rgba(40, 70, 40, 0.18);
  }
  /* Information side */
  .card--info { background: var(--card-white); }
  .brand {
    position: absolute; left: 48px; top: 44px;
    display: flex; align-items: center; gap: 18px;
  }
  .brand__dot {
    flex: none;
    width: 64px; height: 64px; border-radius: 50%;
    background: var(--brand-orange);
  }
  .brand__name {
    color: var(--brand-navy); font-weight: 600; font-size: 26px;
    letter-spacing: 0.12em; text-transform: uppercase; white-space: nowrap;
  }
  .details {
    position: absolute; right: 48px; bottom: 56px;
    display: flex; align-items: flex-start;
  }
  .person { text-align: right; padding-right: 20px; padding-top: 14px; }
  .person__name { color: var(--brand-navy); font-size: 30px; font-weight: 400; line-height: 1.2; white-space: nowrap; }
  .person__role { color: var(--text-grey); font-size: 19px; margin-top: 4px; }
  .contact {
    border-left: 1.5px solid var(--rule-grey);
    padding-left: 18px;
    color: var(--text-grey); font-size: 19px; line-height: 1.5; white-space: nowrap;
  }
  .contact__label { color: var(--brand-orange); margin-right: 6px; }
  /* Brand side */
  .card--brand {
    background: radial-gradient(ellipse 60% 62% at 50% 50%, #ffffff 0%, #fde8d8 30%, var(--brand-orange-light) 62%, var(--brand-orange) 100%);
    display: flex; align-items: center; justify-content: center; gap: 22px;
  }
  .card--brand .brand__dot { width: 96px; height: 96px; }
  .card--brand .brand__name { color: var(--brand-orange); font-size: 30px; }
</style>
</head>
<body>
  <main class="sheet">
    <section class="card card--info" aria-label="Business card, contact side">
      <div class="brand">
        <span class="brand__dot"></span>
        <span class="brand__name">Korvan Fuel Partners</span>
      </div>
      <div class="details">
        <div class="person">
          <p class="person__name">Peter Morrow</p>
          <p class="person__role">Director</p>
        </div>
        <div class="contact">
          <p><span class="contact__label">W:</span>www.korvanse.com.au</p>
          <p><span class="contact__label">E:</span>pmorrow@korvanse.com.au</p>
          <p>PO Box 347, Larkvale</p>
          <p>QLD, 4812</p>
        </div>
      </div>
    </section>

    <section class="card card--brand" aria-label="Business card, brand side">
      <span class="brand__dot"></span>
      <span class="brand__name">Korvan Fuel Partners</span>
    </section>
  </main>
</body>
</html>
```